Hintergrund Design für Flyer und Plakate für Spanischschule
Kreativ, Kompetent, Profesionell und die Zusammenarbeit war sehr angenehm. Sehr gerne wieder.
Zielgruppe
Erwachsene, Kinder Eltern, Familie,
Schulen und Einrichtungen, Firmen
Aufgabenstellung
Das Layout soll multifunktional sein, das heist in seinen Grundzügen oder leicht abgewandelt soll es für Postkarten, Flyer (DIN A 4 - 3 fach geknickt) und evtl. Plakate (als Hintergrund) Verwendung finden.
Und es soll für verschiedene Projekte / Veranstaltungen wiederverwendet werden.

```html
<!DOCTYPE html>
<html lang="de">
<head>
<meta charset="utf-8">
<title>Casa Idioma – Hintergrund</title>
<link href="https://fonts.googleapis.com/css2?family=Amatic+SC:wght@700&display=swap" rel="stylesheet">
<style>
  :root {
    --orange-base: #e6612a;
    --orange-deep: #d6501f;
    --orange-light: #ef8136;
    --orange-glow: #f4a043;
    --white: #ffffff;
    --brand-orange: #ee9a1c;
  }
  html, body {
    margin: 0;
    padding: 0;
    overflow: hidden;
    background: var(--orange-base);
  }
  .poster {
    position: relative;
    width: 848px;
    height: 1200px;
    overflow: hidden;
    background:
      repeating-linear-gradient(180deg,
        transparent 0 22px,
        rgba(214, 80, 31, 0.55) 22px 30px,
        transparent 30px 51px,
        rgba(239, 129, 54, 0.6) 51px 56px,
        transparent 56px 83px,
        rgba(244, 160, 67, 0.35) 83px 86px,
        transparent 86px 117px),
      repeating-linear-gradient(180deg,
        transparent 0 40px,
        rgba(239, 129, 54, 0.45) 40px 61px,
        transparent 61px 97px,
        rgba(200, 72, 26, 0.35) 97px 104px,
        transparent 104px 149px),
      linear-gradient(180deg, var(--orange-base) 0%, var(--orange-light) 45%, var(--orange-base) 70%, var(--orange-deep) 100%);
  }
  .glow-band {
    position: absolute;
    left: 0;
    width: 848px;
    height: 6px;
    background: var(--orange-glow);
    opacity: 0.55;
  }
  .bubbles {
    position: absolute;
    inset: 0;
  }
  .vertical-title {
    position: absolute;
    left: -14px;
    bottom: -12px;
    margin: 0;
    writing-mode: vertical-rl;
    transform: rotate(180deg);
    font-family: "Amatic SC", "Comic Sans MS", cursive;
    font-weight: 700;
    font-size: 150px;
    line-height: 1;
    letter-spacing: 6px;
    color: var(--white);
    white-space: nowrap;
  }
  .brand-name {
    position: absolute;
    left: 560px;
    top: 150px;
    width: 220px;
    margin: 0;
    text-align: center;
    font-family: "Amatic SC", "Comic Sans MS", cursive;
    font-weight: 700;
    font-size: 58px;
    line-height: 0.95;
    color: var(--brand-orange);
  }
  .brand-mark {
    position: absolute;
    left: 650px;
    top: 110px;
    width: 36px;
    height: 36px;
    border-radius: 50%;
    background: var(--brand-orange);
  }
</style>
</head>
<body>
  <main class="poster">
    <div class="glow-band" style="top:210px"></div>
    <div class="glow-band" style="top:440px;height:4px"></div>
    <div class="glow-band" style="top:655px"></div>
    <div class="glow-band" style="top:900px;height:8px"></div>
    <div class="glow-band" style="top:1110px;height:5px"></div>

    <svg class="bubbles" width="848" height="1200" viewBox="0 0 848 1200" aria-hidden="true">
      <g fill="none" stroke="var(--white)" stroke-width="6" stroke-linecap="round" stroke-linejoin="round">
        <!-- top centre bubble -->
        <path d="M420 -10 C405 20 420 52 470 56 L478 82 L492 56 C530 54 540 20 528 -10"/>
        <!-- top right partial bubble -->
        <path d="M778 -10 C785 20 810 38 830 40 L838 62 L846 40"/>
        <!-- right edge bubble -->
        <path d="M852 318 C800 312 738 322 740 370 C742 412 790 420 812 418 L808 446 L832 420 C840 420 848 419 852 418"/>
        <!-- left bubble above title -->
        <path d="M40 240 C80 205 130 215 135 262 C138 300 105 318 78 318 L58 345 L60 315"/>
      </g>
      <!-- brand bubble -->
      <path d="M668 72 C760 70 812 122 808 195 C804 268 748 312 672 314 L660 346 L642 312 C570 304 528 258 530 192 C532 118 585 74 668 72 Z"
            fill="var(--white)"/>
    </svg>

    <span class="brand-mark" aria-hidden="true"></span>
    <p class="brand-name">CASA IDIOMA</p>

    <h1 class="vertical-title">CASA IDIOMA</h1>
  </main>
</body>
</html>
```